Eye-catching Yellow Page Ad for Attorney's Office

We need a phone book advertisement for our law office. We practice workers' compensation law, and our clientele consists exclusively of individuals who have been injured on the job. The dimensions of the print ad will be 6" W X 4.54" H.

We've had our current ad for several years, and wanted to get a new one that has been designed by a professional. Being that it's an ad for a law firm, it needs to be professional looking, but we're hoping to have something that looks a little more modern and has eye-catching appeal. We like the text that is included in the ad, and we want to make sure our phone number is very visible. No real preference for color scheme.

I've attached a copy of our current ad. All the information included in there is accurate. Our office name is Thornbury & Lisle, PLLC. The ethical rules for attorney advertising require the PLLC to be included in the ad, but it can be smaller than the other text (see our current ad).

Target Market(s)

Our potential clients are injured workers looking for legal representation in their workers' compensation claim.

Industry/Entity Type

Attorney

Font styles to use
Serif
Sans Serif

Requirements
Must have
• Professional, but stands out from the crowd
Nice to have
• Clean modern design
Should not have
• We don't want it to be too crowded or over-worked.

```html
<!DOCTYPE html>
<html lang="en">
<head>
<meta charset="UTF-8">
<title>Thornbury &amp; Lisle, PLLC — Workers Compensation</title>
<link href="https://fonts.googleapis.com/css2?family=Roboto+Condensed:wght@700&display=swap" rel="stylesheet">
<style>
  :root {
    --gold: #fdc600;
    --ink: #000000;
    --text-dark: #2a2a2a;
    --paper: #ffffff;
    --photo-tone-a: #8a5a2e;
    --photo-tone-b: #c49a5c;
  }
  * { margin: 0; padding: 0; box-sizing: border-box; }
  html, body { width: 1200px; height: 910px; overflow: hidden; background: var(--paper); }
  body { font-family: "Roboto Condensed", "Arial Narrow", sans-serif; font-weight: 700; }

  .ad { position: relative; width: 1200px; height: 910px; display: flex; overflow: hidden; }

  .ad__side { position: relative; width: 522px; height: 100%; background: var(--gold); }
  .ad__main { position: relative; flex: 1; height: 100%; background: var(--ink); color: var(--paper); }

  .team-photo {
    position: absolute; left: 58px; top: 37px; width: 405px; height: 372px;
    border: 4px solid var(--paper);
    background: linear-gradient(135deg, var(--photo-tone-a) 0%, var(--photo-tone-b) 55%, var(--photo-tone-a) 100%);
  }

  .team-names {
    position: absolute; left: 60px; top: 422px;
    font-size: 33px; color: var(--text-dark); letter-spacing: 0.2px;
  }

  .services { position: absolute; left: 64px; top: 497px; list-style: none; }
  .services li {
    display: flex; align-items: center; height: 54.5px;
    font-size: 28px; color: var(--text-dark);
  }
  .services li::before {
    content: ""; width: 18px; height: 18px; background: var(--paper);
    margin-right: 18px; flex: none;
  }

  .firm-name {
    position: absolute; left: 30px; top: 48px; width: 620px; text-align: center;
    font-size: 74px; line-height: 1; letter-spacing: -0.5px;
  }
  .firm-name__suffix {
    position: absolute; right: 30px; top: 124px; font-size: 14px; letter-spacing: 0.3px;
  }

  .intro {
    position: absolute; left: 28px; top: 190px; width: 606px;
    font-size: 24px; line-height: 40px; text-align: justify;
  }

  .offer-lead {
    position: absolute; left: 0; top: 462px; width: 678px; text-align: center;
    font-size: 60px; line-height: 1;
  }
  .offer-focus {
    position: absolute; left: 0; top: 556px; width: 678px; text-align: center;
    font-size: 52px; line-height: 1; color: var(--gold);
  }

  .phone {
    position: absolute; left: 36px; top: 700px; display: flex; align-items: center;
    font-size: 92px; line-height: 1; letter-spacing: -1px;
  }
  .phone svg { width: 66px; height: 66px; margin-right: 6px; }

  .contact-line {
    position: absolute; left: 0; width: 678px; text-align: center;
    font-size: 29px; line-height: 1; font-weight: 400;
  }
  .contact-line .label { color: var(--gold); }
  .contact-line--address { top: 800px; }
  .contact-line--web { top: 846px; }
</style>
</head>
<body>
  <div class="ad">
    <section class="ad__side">
      <div class="team-photo" role="img" aria-label="Photo of the two attorneys standing in a law library, one holding an open book"></div>
      <p class="team-names">Owen Thornbury &amp; Kara Lisle</p>
      <ul class="services">
        <li>Workplaces Injuries or Death</li>
        <li>Lost Wages</li>
        <li>Medical Expenses &amp; Treatment</li>
        <li>Hearing Loss Claims</li>
        <li>Pension Claims</li>
        <li>Disability Awards</li>
        <li>Return to Work Issues</li>
      </ul>
    </section>

    <section class="ad__main">
      <h1 class="firm-name">Thornbury &amp; Lisle</h1>
      <span class="firm-name__suffix">PLLC</span>

      <p class="intro">Former Assistant Attorneys General Who Know The System At Thornbury &amp; Lisle, We provide personal attention to our clients, That means your case is handled by an attorney not an assistant.</p>

      <p class="offer-lead">WE CAN HELP YOU WITH</p>
      <p class="offer-focus">WORKERS COMPENSATION</p>

      <p class="phone">
        <svg viewBox="0 0 66 66" aria-hidden="true">
          <circle cx="33" cy="33" r="30" fill="none" stroke="#fff" stroke-width="4"/>
          <path d="M22 17c2-1 4 0 5 2l3 6c1 2 0 3-1 4l-2 2c2 4 5 7 9 9l2-2c1-1 2-2 4-1l6 3c2 1 3 3 2 5l-2 4c-1 2-3 3-6 2-12-3-21-12-24-24-1-3 0-5 2-6z" fill="#fff"/>
        </svg>
        360-555-0142
      </p>

      <p class="contact-line contact-line--address"><span class="label">Reach:</span> 245 W. Harbor Street Suite 410, Ferndale</p>
      <p class="contact-line contact-line--web"><span class="label">website:</span> www.thornburylisle.com</p>
    </section>
  </div>
</body>
</html>
```